sticker of engine oil bottle

Dear Designers
i want to design new sticker for my bottle engine oil brand
i want the sticker creative and get harmonic with the bottle color one Blue and another color Red
my brand name is (Vesko) as attached logo and pictures and i will attached pictures you can take ideas from it
The Shape of Plastic bottle i used is the first bottle attached in blue color Vesko 20W50 and in red color vesko 5W30
i want new creative design calms colors and designs
and not copy paste from another design

Target Market(s)

car care and engine oil service centers

Requirements
Must have
• companies approvals and certificates
Nice to have
• new idea
Should not have
• copy past from another design on internet

```html
<!DOCTYPE html>
<html lang="en">
<head>
<meta charset="utf-8">
<title>Vesko — Design No. 02</title>
<link rel="stylesheet" href="https://fonts.googleapis.com/css2?family=Anton&family=Barlow+Condensed:ital,wght@1,600;1,700&family=Inter:wght@500&display=swap">
<style>
  :root {
    --ink: #000000;
    --paper: #ffffff;
    --gold: #e4a61b;
    --label-dark: #0b0d12;
    --bottle-blue: #2f62ad;
    --bottle-red: #c1161d;
    --stripe-blue: #1d3f8a;
    --stripe-red: #7a1018;
  }
  html, body {
    margin: 0;
    width: 1200px;
    height: 675px;
    overflow: hidden;
    background: var(--ink);
  }
  .board {
    position: relative;
    width: 1200px;
    height: 675px;
    background: var(--ink);
    color: var(--paper);
  }
  .brand {
    position: absolute;
    left: 62px;
    top: 84px;
    display: flex;
    align-items: center;
    gap: 10px;
  }
  .brand-dot {
    width: 46px;
    height: 46px;
    border-radius: 50%;
    background: var(--paper);
  }
  .brand-name {
    font-family: "Anton", sans-serif;
    font-size: 60px;
    line-height: 1;
    letter-spacing: 2px;
    color: var(--paper);
  }
  .date {
    position: absolute;
    left: 62px;
    top: 154px;
    margin: 0;
    font-family: "Anton", sans-serif;
    font-size: 11px;
    letter-spacing: 0.2px;
  }
  .design-label {
    position: absolute;
    left: 62px;
    top: 298px;
    font-family: "Anton", sans-serif;
    font-size: 42px;
    line-height: 1;
    transform: scaleX(0.82);
    transform-origin: left;
  }
  .design-number {
    position: absolute;
    left: 255px;
    top: 206px;
    font-family: "Anton", sans-serif;
    font-size: 150px;
    line-height: 1;
    letter-spacing: 2px;
    transform: scaleX(0.8);
    transform-origin: left;
  }
  .notes-title {
    position: absolute;
    left: 64px;
    top: 418px;
    font-family: "Anton", sans-serif;
    font-size: 34px;
    line-height: 1;
    transform: scaleX(0.82);
    transform-origin: left;
  }
  .notes-list {
    position: absolute;
    left: 169px;
    top: 419px;
    width: 215px;
    margin: 0;
    padding: 0;
    list-style: none;
    font-family: "Inter", sans-serif;
    font-weight: 500;
    font-size: 11.2px;
    line-height: 14px;
    letter-spacing: -0.4px;
  }
  .notes-list li { margin-bottom: 13px; }
  .mockup {
    position: absolute;
    top: 89px;
    width: 351px;
    height: 497px;
  }
  .mockup--blue { left: 410px; background: var(--bottle-blue); }
  .mockup--red { left: 784px; background: var(--bottle-red); }
  .label {
    position: absolute;
    left: 50px;
    top: 140px;
    width: 236px;
    height: 302px;
  }
  .label-brand { font-family: "Anton", sans-serif; }
  .label-italic { font-family: "Barlow Condensed", sans-serif; font-style: italic; font-weight: 700; }
  .label-spec { font-family: "Barlow Condensed", sans-serif; font-style: italic; font-weight: 600; }
</style>
</head>
<body>
<main class="board">
  <header class="brand">
    <span class="brand-dot"></span>
    <span class="brand-name">VESKO</span>
  </header>
  <p class="date">1/21/2025</p>

  <div class="design-label">DESIGN NO.</div>
  <div class="design-number">02</div>

  <div class="notes-title">NOTES:</div>
  <ol class="notes-list">
    <li>1. Certifications shown are US-based and I need the images of your company's certification</li>
    <li>2.Every aspect is changeable to desired color/size/specifications</li>
    <li>3. Will also be needing Company Assets; Logos,etc. if designs are chosen. Current logos shown are just manufactured by me.</li>
  </ol>

  <section class="mockup mockup--blue">
    <svg class="label" viewBox="0 0 250 320" aria-label="Vesko 20W50 bottle label">
      <defs>
        <linearGradient id="tone-blue" x1="0" y1="0" x2="1" y2="1">
          <stop offset="0" stop-color="var(--label-dark)"/>
          <stop offset="0.55" stop-color="var(--stripe-blue)"/>
          <stop offset="1" stop-color="var(--label-dark)"/>
        </linearGradient>
        <linearGradient id="grade-plate" x1="0" y1="0" x2="1" y2="0">
          <stop offset="0" stop-color="#b9b9b9"/>
          <stop offset="1" stop-color="#2b2b2b"/>
        </linearGradient>
      </defs>
      <path d="M20,0 H150 L248,255 Q258,298 215,303 L22,320 Q0,322 0,300 V20 Q0,0 20,0 Z" fill="url(#tone-blue)" stroke="#1a1a1a" stroke-width="3"/>
      <text class="label-brand" transform="translate(60,232) rotate(-90)" font-size="62" fill="#fff" textLength="205" lengthAdjust="spacingAndGlyphs">VESKO</text>
      <text class="label-italic" transform="translate(80,100) rotate(-90)" font-size="12" fill="#fff" letter-spacing="1">LUBRICANTS</text>
      <circle cx="152" cy="122" r="48" fill="none" stroke="var(--gold)" stroke-width="14"/>
      <rect x="82" y="186" width="148" height="48" fill="url(#grade-plate)"/>
      <text class="label-brand" x="88" y="228" font-size="44" fill="#fff">20W50</text>
      <text class="label-italic" x="20" y="256" font-size="12" fill="#fff">HIGH PERFORMANCE PETROL ENGINE OIL</text>
      <text class="label-italic" x="196" y="256" font-size="10" fill="var(--gold)">+</text>
      <text class="label-italic" x="204" y="252" font-size="4.5" fill="var(--gold)">HIGH</text>
      <text class="label-italic" x="204" y="257" font-size="4.5" fill="var(--gold)">EFFICIENCY</text>
      <circle cx="26" cy="283" r="12" fill="none" stroke="#fff" stroke-width="1.5"/>
      <circle cx="54" cy="283" r="12" fill="#fff"/>
      <circle cx="82" cy="283" r="12" fill="none" stroke="#fff" stroke-width="2"/>
      <text class="label-spec" x="100" y="272" font-size="5.5" fill="#fff">MEETS THE REQUIREMENTS OF:</text>
      <text class="label-spec" x="100" y="280" font-size="5.5" fill="var(--gold)">DX 229.1  KRT M 271  NRV 15811</text>
      <text class="label-spec" x="100" y="287" font-size="5.5" fill="var(--gold)">ALVERN C4  NORVIK VDS  TERRAPIN TO-2</text>
      <text class="label-spec" x="100" y="295" font-size="5.5" fill="#fff">PQI SL/CF | EQS A3/B4</text>
      <text class="label-spec" x="100" y="301" font-size="5.5" fill="var(--gold)">MINERAL</text>
      <circle cx="212" cy="282" r="15" fill="var(--label-dark)" stroke="var(--gold)" stroke-width="2.5"/>
      <text class="label-brand" x="212" y="290" font-size="19" fill="var(--gold)" text-anchor="middle">5L</text>
    </svg>
  </section>

  <section class="mockup mockup--red">
    <svg class="label" viewBox="0 0 250 320" aria-label="Vesko 5W30 bottle label">
      <defs>
        <linearGradient id="tone-red" x1="0" y1="0" x2="1" y2="1">
          <stop offset="0" stop-color="var(--label-dark)"/>
          <stop offset="0.55" stop-color="var(--stripe-red)"/>
          <stop offset="1" stop-color="var(--label-dark)"/>
        </linearGradient>
        <linearGradient id="grade-plate-red" x1="0" y1="0" x2="1" y2="0">
          <stop offset="0" stop-color="#b9b9b9"/>
          <stop offset="1" stop-color="#2b2b2b"/>
        </linearGradient>
      </defs>
      <path d="M20,0 H150 L248,255 Q258,298 215,303 L22,320 Q0,322 0,300 V20 Q0,0 20,0 Z" fill="url(#tone-red)" stroke="#1a1a1a" stroke-width="3"/>
      <text class="label-brand" transform="translate(60,232) rotate(-90)" font-size="62" fill="#fff" textLength="205" lengthAdjust="spacingAndGlyphs">VESKO</text>
      <text class="label-italic" transform="translate(80,100) rotate(-90)" font-size="12" fill="#fff" letter-spacing="1">LUBRICANTS</text>
      <circle cx="152" cy="122" r="48" fill="none" stroke="var(--gold)" stroke-width="14"/>
      <rect x="82" y="186" width="148" height="48" fill="url(#grade-plate-red)"/>
      <text class="label-brand" x="92" y="228" font-size="44" fill="#fff">5W30</text>
      <text class="label-italic" x="20" y="256" font-size="12" fill="#fff">HIGH PERFORMANCE PETROL ENGINE OIL</text>
      <text class="label-italic" x="196" y="256" font-size="10" fill="var(--gold)">+</text>
      <text class="label-italic" x="204" y="252" font-size="4.5" fill="var(--gold)">HIGH</text>
      <text class="label-italic" x="204" y="257" font-size="4.5" fill="var(--gold)">EFFICIENCY</text>
      <circle cx="26" cy="283" r="12" fill="none" stroke="#fff" stroke-width="1.5"/>
      <circle cx="54" cy="283" r="12" fill="#fff"/>
      <circle cx="82" cy="283" r="12" fill="none" stroke="#fff" stroke-width="2"/>
      <text class="label-spec" x="100" y="272" font-size="5.5" fill="#fff">MEETS THE REQUIREMENTS OF:</text>
      <text class="label-spec" x="100" y="280" font-size="5.5" fill="var(--gold)">DX 229.1  KRT M 271  NRV 15811</text>
      <text class="label-spec" x="100" y="287" font-size="5.5" fill="var(--gold)">ALVERN C4  NORVIK VDS  TERRAPIN TO-2</text>
      <text class="label-spec" x="100" y="295" font-size="5.5" fill="#fff">PQI SL/CF | EQS A3/B4</text>
      <text class="label-spec" x="100" y="301" font-size="5.5" fill="var(--gold)">MINERAL</text>
      <circle cx="212" cy="282" r="15" fill="var(--label-dark)" stroke="var(--gold)" stroke-width="2.5"/>
      <text class="label-brand" x="212" y="290" font-size="19" fill="var(--gold)" text-anchor="middle">5L</text>
    </svg>
  </section>
</main>
</body>
</html>
```